" Nossa empresa oferece diversos tipos de soluçoes na área de Gestao de Ativos para empresas do Setor Elétrico Brasileiro. Somos uma empresa Jovem com grandes ambiçoes. Apesar de pequenos, já temos na nossa carteira grandes empresas do setor e nosso objetivo agora é ampliar os serviços nas empresas em que já atuamos e conquistar novos clientes "

```html
<!DOCTYPE html>
<html lang="pt-BR">
<head>
<meta charset="utf-8">
<title>Vantra — Cadastro de notícias</title>
<link href="https://fonts.googleapis.com/css2?family=Open+Sans:wght@400;600;700&display=swap" rel="stylesheet">
<style>
:root{
  --navy:#2c3e55;
  --blue:#4a84c4;
  --blue-dark:#3b6fa8;
  --nav-text:#5a5f66;
  --white:#ffffff;
  --hero-a:#3a4350;
  --hero-b:#76808c;
  --hero-c:#a9b2bb;
  --form-bg:rgba(14,18,24,.82);
  --input-bg:#0d1117;
  --input-text:#8a9099;
}
*{box-sizing:border-box;margin:0;padding:0}
html,body{width:1200px;height:1200px;overflow:hidden;background:var(--white);font-family:"Open Sans",Arial,sans-serif}
.page-variant{position:relative;width:1200px;height:600px;overflow:hidden}
.site-nav{position:absolute;top:0;left:0;width:1200px;height:72px;background:var(--white);border-bottom:1px solid #e3e6ea}
.brand{position:absolute;left:96px;top:12px;display:flex;align-items:center;gap:12px}
.brand-dot{width:26px;height:26px;border-radius:50%;background:var(--blue)}
.brand-name{font-size:40px;font-weight:700;color:var(--navy);line-height:48px;letter-spacing:-.5px}
.nav-link{position:absolute;top:0;height:72px;line-height:74px;font-size:13px;font-weight:600;color:var(--nav-text);letter-spacing:.6px;text-transform:uppercase}
.nav-link.is-active{color:var(--blue)}
.nav-link.is-active::after{content:"";position:absolute;left:-8px;right:-8px;bottom:0;height:4px;background:var(--blue)}
.search-box{position:absolute;left:936px;top:24px;width:186px;height:26px;background:var(--blue);border-radius:2px}
.search-box svg{position:absolute;left:6px;top:6px}
.hero{position:absolute;top:72px;left:0;width:1200px;height:528px}
.hero-photo{position:absolute;inset:0;background:
  radial-gradient(ellipse 260px 320px at 300px 330px,rgba(30,36,46,.75),transparent 70%),
  radial-gradient(ellipse 320px 260px at 950px 320px,rgba(40,48,60,.6),transparent 70%),
  linear-gradient(180deg,var(--hero-c) 0%,var(--hero-b) 40%,var(--hero-a) 100%)}
.hero-shade{position:absolute;inset:0;background:rgba(20,26,34,.28)}
.hero-title{position:absolute;top:112px;left:0;width:1200px;text-align:center;font-size:52px;font-weight:600;color:var(--white);letter-spacing:-.3px}
.hero-lead{position:absolute;top:200px;left:205px;width:790px;text-align:center;font-size:19px;line-height:27px;color:var(--white)}
.signup-form{position:absolute;top:288px;left:197px;width:806px;height:84px;background:var(--form-bg)}
.field{position:absolute;top:19px;width:184px;height:46px;background:var(--input-bg);border-left:3px solid var(--blue);border-bottom:1px solid #3c4450;font-size:13px;line-height:44px;padding-left:14px;color:var(--input-text)}
.submit-btn{position:absolute;top:19px;left:631px;width:158px;height:46px;background:var(--blue);color:var(--white);font-size:13px;font-weight:700;line-height:46px;text-align:center;letter-spacing:.2px}
.cta-note{position:absolute;top:394px;left:725px;font-size:13px;color:var(--white)}
.cta-arrow{position:absolute;top:370px;left:862px}
.slider-arrow{position:absolute;top:466px}
.slider-dots{position:absolute;top:492px;left:560px;display:flex;gap:6px}
.slider-dots span{width:10px;height:10px;border-radius:50%;border:1.5px solid var(--white)}
.slider-dots span.is-current{background:var(--white)}
</style>
</head>
<body>

<section class="page-variant">
  <header class="site-nav">
    <div class="brand"><span class="brand-dot"></span><span class="brand-name">Vantra</span></div>
    <span class="nav-link" style="left:355px">Página inicial</span>
    <span class="nav-link is-active" style="left:492px">Sobre nós</span>
    <span class="nav-link" style="left:598px">O que fazemos</span>
    <span class="nav-link" style="left:728px">Parceiros</span>
    <span class="nav-link" style="left:823px">Atendimento</span>
    <div class="search-box"><svg width="14" height="14" viewBox="0 0 14 14"><circle cx="5.5" cy="5.5" r="4" fill="none" stroke="#fff" stroke-width="1.6"/><line x1="8.5" y1="8.5" x2="12.5" y2="12.5" stroke="#fff" stroke-width="1.6"/></svg></div>
  </header>
  <div class="hero">
    <div class="hero-photo" role="img" aria-label="Foto de executivos de terno em ambiente corporativo, com fundo desfocado"></div>
    <div class="hero-shade"></div>
    <h1 class="hero-title">Quer receber todas as notícias?</h1>
    <p class="hero-lead">Preencha abaixo seu nome, email e telefone e receba todas as novidades, oportunidades e muito mais... Assine</p>
    <div class="signup-form">
      <div class="field" style="left:19px">Seu nome</div>
      <div class="field" style="left:222px">Seu email</div>
      <div class="field" style="left:425px">Seu telefone</div>
      <div class="submit-btn">CADASTRAR DADOS</div>
    </div>
    <span class="cta-note">Assine agora mesmo</span>
    <svg class="cta-arrow" width="40" height="30" viewBox="0 0 40 30"><path d="M2 26 Q20 24 34 6" fill="none" stroke="#fff" stroke-width="1.4"/><path d="M27 7 L34 6 L34 13" fill="none" stroke="#fff" stroke-width="1.4"/></svg>
    <svg class="slider-arrow" style="left:100px" width="16" height="22" viewBox="0 0 16 22"><path d="M12 3 L4 11 L12 19" fill="none" stroke="#fff" stroke-width="3"/></svg>
    <svg class="slider-arrow" style="left:150px" width="16" height="22" viewBox="0 0 16 22"><path d="M4 3 L12 11 L4 19" fill="none" stroke="#fff" stroke-width="3"/></svg>
    <div class="slider-dots"><span></span><span></span><span class="is-current"></span><span></span><span></span></div>
  </div>
</section>

<section class="page-variant">
  <header class="site-nav">
    <div class="brand"><span class="brand-dot"></span><span class="brand-name">Vantra</span></div>
    <span class="nav-link" style="left:355px">Página inicial</span>
    <span class="nav-link is-active" style="left:492px">Sobre nós</span>
    <span class="nav-link" style="left:598px">O que fazemos</span>
    <span class="nav-link" style="left:728px">Parceiros</span>
    <span class="nav-link" style="left:823px">Atendimento</span>
    <div class="search-box"><svg width="14" height="14" viewBox="0 0 14 14"><circle cx="5.5" cy="5.5" r="4" fill="none" stroke="#fff" stroke-width="1.6"/><line x1="8.5" y1="8.5" x2="12.5" y2="12.5" stroke="#fff" stroke-width="1.6"/></svg></div>
  </header>
  <div class="hero">
    <div class="hero-photo" role="img" aria-label="Foto de executivos de terno em ambiente corporativo, com fundo desfocado"></div>
    <div class="hero-shade"></div>
    <h1 class="hero-title">Quer receber todas as notícias?</h1>
    <p class="hero-lead">Preencha abaixo seu nome, email e telefone e receba todas as novidades, oportunidades e muito mais... Assine</p>
    <div class="signup-form">
      <div class="field" style="left:19px">Seu nome</div>
      <div class="field" style="left:222px">Seu email</div>
      <div class="field" style="left:425px">Seu telefone</div>
      <div class="submit-btn">CADASTRAR DADOS</div>
    </div>
    <span class="cta-note">Assine agora mesmo</span>
    <svg class="cta-arrow" width="40" height="30" viewBox="0 0 40 30"><path d="M2 26 Q20 24 34 6" fill="none" stroke="#fff" stroke-width="1.4"/><path d="M27 7 L34 6 L34 13" fill="none" stroke="#fff" stroke-width="1.4"/></svg>
    <svg class="slider-arrow" style="left:100px" width="16" height="22" viewBox="0 0 16 22"><path d="M12 3 L4 11 L12 19" fill="none" stroke="#fff" stroke-width="3"/></svg>
    <svg class="slider-arrow" style="left:150px" width="16" height="22" viewBox="0 0 16 22"><path d="M4 3 L12 11 L4 19" fill="none" stroke="#fff" stroke-width="3"/></svg>
    <div class="slider-dots"><span></span><span></span><span class="is-current"></span><span></span><span></span></div>
  </div>
</section>

</body>
</html>
```